K9 Orbit needs a business card designed

We need a business card designed for K9 Orbit, an expansion of K9 Systems Pty Ltd (www.k9orbit.com.au)

We provide high quality professional services for the Australian space industry. Our clients include the Southern Launch Bureau and companies working in the space industry. We identify people with space related skills both locally and internationally who are then contracted by clients to create products and support space launch activities.

Colours to be used:
- Navy blue #000080
- Rocket metallic #8A7F8D
- Platinum #E5E4E2
- Black #000000
- White #FFFFFF

*Front of the card*
I have attached our K9 Orbit logo, which needs to be the main item on the card. The 'Space' text should be placed to the right of the 'K9' part rather than below, similar to the attached K9 Systems card, which this card should match.

If subtext is included, however, it should read ‘Labour Hire • Consultancy • Project Delivery’ rather than the ‘Labour Hire • Consultancy • Project Delivery’ of the K9 Systems card.

A black background (rather than blue background in the K9 Systems card) might be good, with a white pattern as in the K9 Systems card. If colour is used, the logo should be in its standard colours (as provided for the K9 Orbit logo).

*Back of the card*
Include a smaller K9 Orbit logo on the back.

We need the following details for K9 Orbit personnel (as a template for entry):
- Name
- Company Position
- Mobile Number
- Email
- Office Address
- Include the K9 Orbit website: www.k9orbit.com.au

Overall, we'd like to see a design that communicates the adventure of space, professional integrity, and customer service. We look forward to seeing what you can come up with.

Target Market(s)

We provide high quality professional services for the Australian space industry. Our clients include the Southern Launch Bureau and companies working in the space industry.

Contact Information for Business Card

- Name
- Company Position
- Mobile Number
- Email
- Office Address

Requirements
Must have
• See project description.

```html
<!DOCTYPE html>
<html lang="en">
<head>
<meta charset="utf-8">
<title>K9 Orbit business cards</title>
<link href="https://fonts.googleapis.com/css2?family=Montserrat:wght@400;500;600&family=Roboto:wght@400;500&display=swap" rel="stylesheet">
<style>
  :root {
    --page: #3a3431;
    --card: #121314;
    --card-back: #16181b;
    --orbit-blue: #3b3bb0;
    --accent-blue: #1f7fd6;
    --white: #ffffff;
    --platinum: #e5e4e2;
  }
  * { box-sizing: border-box; margin: 0; padding: 0; }
  html, body { width: 1200px; height: 716px; overflow: hidden; }
  body {
    background: var(--page);
    position: relative;
    font-family: "Roboto", Arial, sans-serif;
  }
  .card {
    position: absolute;
    top: 215px;
    width: 500px;
    height: 286px;
    border-radius: 6px;
    box-shadow: 0 10px 28px rgba(0,0,0,.45);
    overflow: hidden;
  }
  .card-front { left: 60px; background: var(--card); }
  .card-back { left: 640px; background: var(--card-back); color: var(--white); }

  .front-logo {
    position: absolute;
    inset: 0;
    display: flex;
    align-items: center;
    justify-content: center;
    gap: 14px;
  }
  .front-logo .mark {
    width: 30px; height: 30px; border-radius: 50%;
    background: var(--orbit-blue);
  }
  .front-logo .name {
    font-family: "Montserrat", Arial, sans-serif;
    font-weight: 600;
    font-size: 46px;
    letter-spacing: 6px;
    color: var(--orbit-blue);
  }

  .back-brand {
    position: absolute;
    top: 30px; right: 28px;
    text-align: right;
  }
  .back-brand .row { display: flex; align-items: center; gap: 8px; justify-content: flex-end; }
  .back-brand .mark { width: 16px; height: 16px; border-radius: 50%; background: var(--accent-blue); }
  .back-brand .name {
    font-family: "Montserrat", Arial, sans-serif;
    font-weight: 400; font-size: 24px; color: var(--white);
  }
  .back-brand .tagline {
    margin-top: 4px;
    font-family: "Montserrat", Arial, sans-serif;
    font-size: 7px; letter-spacing: .4px; color: var(--accent-blue);
  }

  .person {
    position: absolute; left: 34px; top: 96px;
    padding-left: 14px;
    border-left: 5px solid var(--accent-blue);
  }
  .person .name {
    font-family: "Montserrat", Arial, sans-serif;
    font-weight: 500; font-size: 20px; letter-spacing: 1.5px; line-height: 22px;
    color: var(--accent-blue); text-transform: uppercase;
  }
  .person .role { font-size: 11px; color: var(--platinum); margin-top: 3px; }

  .divider {
    position: absolute; left: 53px; right: 36px; top: 146px;
    height: 1px; background: var(--accent-blue);
  }

  .contacts {
    position: absolute; left: 34px; top: 156px;
    list-style: none; font-size: 12px; line-height: 20px; color: var(--platinum);
  }
  .contacts li { display: flex; align-items: center; gap: 7px; }
  .contacts svg { width: 10px; height: 10px; fill: var(--accent-blue); flex: none; }

  .address-rule {
    position: absolute; left: 53px; right: 36px; bottom: 68px;
    height: 1px; background: var(--accent-blue); opacity: .6;
  }
  .address {
    position: absolute; right: 34px; bottom: 24px;
    text-align: right; font-size: 13px; line-height: 18px; color: var(--platinum);
    font-style: normal;
  }
</style>
</head>
<body>
  <section class="card card-front" aria-label="Card front">
    <div class="front-logo">
      <span class="mark"></span>
      <span class="name">K9 ORBIT</span>
    </div>
  </section>

  <section class="card card-back" aria-label="Card back">
    <div class="back-brand">
      <div class="row"><span class="mark"></span><span class="name">K9 Orbit</span></div>
      <div class="tagline">Labour Hire • Consultancy • Project Delivery</div>
    </div>

    <div class="person">
      <div class="name">Darren Kellow</div>
      <div class="role">Director</div>
    </div>
    <div class="divider"></div>

    <ul class="contacts">
      <li><svg viewBox="0 0 10 10"><path d="M2 0.5 L3.6 2.6 L2.8 3.6 Q3.8 5.6 6.2 7 L7.3 6.2 L9.5 7.8 L8.4 9.5 Q3.5 9 0.5 1.8 Z"/></svg>+61 400 512 738</li>
      <li><svg viewBox="0 0 10 10"><path d="M0 2 H10 V8.5 H0 Z M0.6 2.4 L5 5.6 L9.4 2.4" stroke="#16181b" stroke-width=".7"/></svg>hello@k9orbit.com.au</li>
      <li><svg viewBox="0 0 10 10"><circle cx="5" cy="5" r="4.5" fill="none" stroke="#1f7fd6" stroke-width="1"/><path d="M0.5 5 H9.5 M5 0.5 V9.5" stroke="#1f7fd6" stroke-width=".8"/></svg>www.k9orbit.com.au</li>
    </ul>

    <div class="address-rule"></div>
    <address class="address">
      Suite 7, 48 Harlow St<br>
      Port Avery VIC 3999
    </address>
  </section>
</body>
</html>
```